New, modern business card for growing audiology practice

We need a new business card for our audiology practice. Our logo and website have recently changed (more modern) and we want our business cards to reflect this change.
We conduct hearing tests, perform earwax removals, and fit & dispense hearing aids to our patients. We are a family owned practice in which the owner is the one who works directly with the patient. I have attached logos in various formats to use, as well as two ideas I found on this website; as well as a scanned copy of our current logo. Good luck!

Industry/Entity Type

Business

Contact Information for Business Card

Company name: Birchmont Hearing Center
Provider name: Peter Lowsby, Au.D. F/NSO
Phone number: (555) 318-6042
Address: 287 W. Hollister Rd. Larkfield Falls, OH 40000
email: birchmonthearing@quillpost.net
website: birchmonthearing.net

Colors
000000
aaaaaa
dbdbdb
cacaca
9bcb3c
afd23c
cadf82
b1b1b1

Requirements
Must have
• My card must include information in the "details" section. In the attached images, I found a few that I liked and I would like to model after - "steady strivin'" and "Sound Lab Clinic".
• Must be horizontal.
• Must include logos provided. I uploaded them in various file formats and various ways.
• Must match logo font, if possible, if not, please get as close as you can.
Nice to have
• I really like the idea of having a color on one side with just the logo and company name and the contact information and provider name on the other side. I also really like the idea of having the main color dominating on the logo/company side with accent of that same color on the contact side of the card.
Should not have
• Must not be vertical.

```html
<!DOCTYPE html>
<html lang="en">
<head>
<meta charset="utf-8">
<title>Birchmont Hearing Center – Business Card</title>
<link rel="stylesheet" href="https://fonts.googleapis.com/css2?family=Jost:wght@300;400;500&display=swap">
<style>
  :root {
    --stage: #e6e7e8;
    --label: #6d6e70;
    --paper: #ffffff;
    --lime: #cadf82;
    --lime-deep: #c0d779;
    --leaf: #7aab3c;
    --ink: #000000;
    --ink-soft: #1a1a1a;
    --ghost: #f5f7f0;
  }
  * { margin: 0; padding: 0; box-sizing: border-box; }
  html, body { width: 1200px; height: 1200px; overflow: hidden; }
  body {
    background: var(--stage);
    font-family: "Jost", "Futura", sans-serif;
    position: relative;
  }
  .side-label {
    position: absolute;
    left: 227px;
    font-size: 14px;
    font-weight: 400;
    color: var(--label);
    letter-spacing: 0.02em;
  }
  .side-label--front { top: 48px; }
  .side-label--back { top: 605px; }

  .card {
    position: absolute;
    left: 227px;
    width: 747px;
    height: 462px;
    overflow: hidden;
  }
  .card--front { top: 86px; background: var(--paper); }
  .card--back { top: 647px; background: var(--lime); }

  .card__decor {
    position: absolute;
    left: 0; top: 0;
    width: 747px; height: 462px;
  }

  .brand {
    position: absolute;
    left: 0; right: 0;
    display: flex;
    align-items: center;
    justify-content: center;
    color: var(--ink);
    font-weight: 500;
    text-transform: uppercase;
    letter-spacing: -0.01em;
    line-height: 1.2;
  }
  .brand__dot {
    border-radius: 50%;
    background: var(--leaf);
    flex: none;
  }
  .card--front .brand { top: 81px; font-size: 23px; gap: 10px; }
  .card--front .brand__dot { width: 16px; height: 16px; }
  .card--back .brand { top: 212px; font-size: 32px; gap: 15px; }
  .card--back .brand__dot { width: 23px; height: 23px; }

  .provider {
    position: absolute;
    top: 185px;
    left: 0; right: 0;
    text-align: center;
    font-size: 21px;
    font-weight: 500;
    color: var(--ink);
  }
  .contact {
    position: absolute;
    top: 240px;
    left: 0; right: 0;
    text-align: center;
    font-size: 21px;
    font-weight: 300;
    line-height: 29px;
    color: var(--ink-soft);
    font-style: normal;
  }
</style>
</head>
<body>

<p class="side-label side-label--front">FRONT</p>
<section class="card card--front" aria-label="Business card front">
  <svg class="card__decor" viewBox="0 0 747 462" aria-hidden="true">
    <circle cx="630" cy="185" r="150" fill="none" stroke="var(--ghost)" stroke-width="45"/>
    <path d="M0 436 Q 380 442 747 415 L747 462 L0 462 Z" fill="var(--lime)"/>
  </svg>
  <div class="brand"><span class="brand__dot"></span><span>Birchmont Hearing Center</span></div>
  <p class="provider">Peter Lowsby, Au.D. F/NSO</p>
  <address class="contact">
    (555) 318-6042<br>
    287 W. Hollister Rd. Larkfield Falls, OH 40000<br>
    birchmonthearing@quillpost.net<br>
    birchmonthearing.net
  </address>
</section>

<p class="side-label side-label--back">BACK</p>
<section class="card card--back" aria-label="Business card back">
  <svg class="card__decor" viewBox="0 0 747 462" aria-hidden="true">
    <circle cx="620" cy="185" r="150" fill="none" stroke="var(--lime-deep)" stroke-width="45"/>
  </svg>
  <div class="brand"><span class="brand__dot"></span><span>Birchmont Hearing Center</span></div>
</section>

</body>
</html>
```